Copper Hollow Sparkling

Hi all,

Thanks for taking the time to check out our brief.

Copper Hollow is an Australian wine company based in Victoria, and have been around for more than 20 years. We have a well-known sparkling Chardonnay Pinot Noir that needs a package revamp and we need your help!

Check out our current package here: http://www.copperhollowvino.com.au/our-wines/dsp-default_b.cfm?loadref=17

So here's the brief:

1. Use of the Copper Hollow logo (silhouette) and text mandatory - but can be as small/large as required.

2. Design must be shown on a sparkling bottle.

3. Can be closed with cork or crown seal - neck label/hood not mandatory.

4. Front label size to be no larger than 75mm high x 100mm wide. Back label to be no larger than 75mm x 100mm

5. Label does not have to be square/rectangular. Happy to see thoughts outside the box.

6. Design cannot be printed onto the bottle - must be on a label that can be applied to the bottle.

7. Be forward thinking. Be interesting. This design does not have to tie into our still (red and white) wine range.

8. Mandatory information to be shown on front label - a. Wine of Australia - b. Sparkling Chardonnay Pinot Noir

9. Mandatory info for front label - a. 750mL - b. Alcohol e.g. 13.5% ALC/VOL - c. Wine of Australi - d. Producer address (please insert dummy address at this stage - e. standard drinks e.g. approx 8.0 standard drinks (this can also be shown in the standard drinks glass logo) - f. space for a tasting blurb

10. Try to stay away from anything floral or overly girly.

Industry/Entity Type

Floral

Requirements
Must have
• Design must be shown on a sparkling wine bottle & include the full label design separately
Should not have
• Try to stay away from anything too floral and overly girly.

```html
<!DOCTYPE html>
<html lang="en">
<head>
<meta charset="utf-8">
<title>Copper Hollow Sparkling – Labels</title>
<link rel="stylesheet" href="https://fonts.googleapis.com/css2?family=Cinzel:wght@400;500&family=Crimson+Text:ital@1&family=Arimo&display=swap">
<style>
  :root {
    --backdrop: #f4f4f5;
    --wine: #5a1414;
    --wine-deep: #3e0c0c;
    --copper-glow: #c9a27e;
    --pearl: #fbfaf5;
    --pearl-shade: #d9d4c6;
    --ink-brown: #4a2a18;
    --ink-dark: #2c2420;
    --silhouette: #3a3a3a;
    --frame: #9a9a9a;
    --white: #ffffff;
  }
  * { margin: 0; padding: 0; box-sizing: border-box; }
  html, body { width: 1200px; height: 1000px; overflow: hidden; }
  body {
    position: relative;
    background: radial-gradient(ellipse at center, var(--white) 30%, var(--backdrop) 100%);
    font-family: "Arimo", Arial, sans-serif;
  }
  .label-art { position: absolute; inset: 0; }
  .text { position: absolute; color: var(--ink-brown); white-space: nowrap; }
  .brand {
    font-family: "Cinzel", serif; font-weight: 500; color: var(--white);
    text-align: center; letter-spacing: 0.22em;
  }
  .variety { font-family: "Cinzel", serif; font-weight: 400; line-height: 1; }
  .origin { font-family: "Arimo", Arial, sans-serif; color: var(--ink-dark); }

  /* front label */
  .front .brand { left: 440px; width: 360px; top: 148px; font-size: 26px; transform: rotate(-2.5deg); }
  .front .sparkling { left: 432px; width: 370px; text-align: center; top: 205px; font-size: 20px; }
  .front .chardonnay { left: 432px; width: 370px; text-align: center; top: 234px; font-size: 38px; }
  .front .pinot { left: 432px; width: 370px; text-align: center; top: 268px; font-size: 38px; }
  .front .origin { left: 432px; width: 370px; text-align: center; top: 318px; font-size: 12px; }

  /* back label */
  .back .brand { left: 430px; width: 373px; top: 539px; font-size: 22px; }
  .back .sparkling { left: 548px; top: 592px; font-size: 15px; }
  .back .chardonnay { left: 548px; top: 610px; font-size: 28px; }
  .back .pinot { left: 548px; top: 640px; font-size: 28px; }
  .back .origin { left: 548px; top: 668px; font-size: 12px; }
  .back .blurb {
    left: 548px; top: 684px; width: 250px; white-space: normal;
    font-family: "Crimson Text", Georgia, serif; font-style: italic;
    font-size: 12.5px; line-height: 14px; color: var(--ink-dark);
  }
  .back .address { left: 456px; top: 754px; font-size: 12px; line-height: 13.5px; color: var(--ink-dark); }
  .back .volume { left: 720px; top: 754px; font-size: 13px; line-height: 16px; color: var(--ink-dark); text-align: center; width: 60px; }
</style>
</head>
<body>
  <svg class="label-art" width="1200" height="1000" viewBox="0 0 1200 1000">
    <defs>
      <radialGradient id="wineGlow" cx="0.55" cy="1" r="0.7">
        <stop offset="0" stop-color="var(--copper-glow)"/>
        <stop offset="0.45" stop-color="var(--wine)"/>
        <stop offset="1" stop-color="var(--wine-deep)"/>
      </radialGradient>
      <linearGradient id="pearlSheen" x1="0" y1="0" x2="1" y2="1">
        <stop offset="0" stop-color="var(--pearl-shade)"/>
        <stop offset="0.4" stop-color="var(--pearl)"/>
        <stop offset="0.7" stop-color="var(--pearl)"/>
        <stop offset="1" stop-color="var(--pearl-shade)"/>
      </linearGradient>
      <clipPath id="frontShape">
        <path d="M450,118 L785,88 Q802,86 802,104 L800,320 Q800,338 782,342 L455,366 Q437,368 436,350 L432,136 Q432,120 450,118 Z"/>
      </clipPath>
    </defs>

    <!-- front label -->
    <g class="front-label" clip-path="url(#frontShape)">
      <rect x="420" y="80" width="400" height="112" fill="url(#wineGlow)"/>
      <rect x="420" y="190" width="400" height="6" fill="var(--white)"/>
      <rect x="420" y="196" width="400" height="180" fill="url(#pearlSheen)"/>
    </g>
    <path d="M450,118 L785,88 Q802,86 802,104 L800,320 Q800,338 782,342 L455,366 Q437,368 436,350 L432,136 Q432,120 450,118 Z"
          fill="none" stroke="var(--frame)" stroke-width="3"/>

    <!-- back label -->
    <g class="back-label">
      <rect x="430" y="530" width="373" height="280" fill="url(#pearlSheen)"/>
      <rect x="430" y="530" width="373" height="38" fill="url(#wineGlow)"/>
      <rect x="430" y="568" width="373" height="8" fill="var(--white)"/>
      <rect x="440" y="585" width="92" height="160" rx="6" fill="var(--silhouette)"
            role="img" aria-label="Brand silhouette illustration of standing figures"/>
      <rect x="582" y="760" width="30" height="24" rx="3" fill="var(--ink-dark)"
            role="img" aria-label="Standard drinks symbol"/>
    </g>
  </svg>

  <div class="front">
    <div class="text brand">COPPER HOLLOW</div>
    <div class="text variety sparkling">SPARKLING</div>
    <div class="text variety chardonnay">CHARDONNAY</div>
    <div class="text variety pinot">PINOT NOIR</div>
    <div class="text origin">Wine of Australia</div>
  </div>

  <div class="back">
    <div class="text brand">COPPER HOLLOW</div>
    <div class="text variety sparkling">SPARKLING</div>
    <div class="text variety chardonnay">CHARDONNAY</div>
    <div class="text variety pinot">PINOT NOIR</div>
    <div class="text origin">Wine of Australia</div>
    <p class="text blurb">Enjoy a premium non-vintage wine made from selected Chardonnay and Pinot Noir grapes, displaying classic citrus flavours with a delicate crisp finish.</p>
    <div class="text address">PO Box 1000<br>Larkwood<br>VIC 3999<br>Australia</div>
    <div class="text volume">750mL<br>13.5%<br>ALC/VOL</div>
  </div>
</body>
</html>
```